Corporate brochures for christmas parties

I need to get multiple brochures made and looking for a design that we can roll across all brochures using the same template but with different content. We are looking to have one made initially and then if we like the design have all the brochures made. I have included some samples below. We only send these out as PDFS - they need to be A4 - would be interested in either landscape or portraint designs.

Target Market(s)

Corporate event buyers

Industry/Entity Type

Events

Font styles to use
Sans Serif

Requirements
Must have
• About the event
• About the venue
• Whats included page
• Image Gallery
• Dates and Prices page
• Location page

```html
<!DOCTYPE html>
<html lang="en">
<head>
<meta charset="utf-8">
<title>Christmas Party Brochure – Template Spreads</title>
<link href="https://fonts.googleapis.com/css2?family=Poiret+One&family=Raleway:wght@400;600&display=swap" rel="stylesheet">
<style>
  :root{
    --paper:#ffffff;
    --plum-deep:#2a0c36;
    --plum:#4a1452;
    --magenta:#9a1f80;
    --band:rgba(26,4,34,0.42);
    --ink:#ffffff;
    --ink-soft:#e6d3ea;
    --rule:rgba(255,255,255,0.35);
    --photo-a:#3b1f6e;
    --photo-b:#c23a8a;
    --photo-dark:#1a0a14;
    --map-land:#e8e0d2;
    --pin:#e0207a;
  }
  *{box-sizing:border-box;margin:0;padding:0}
  html,body{width:1200px;height:929px;overflow:hidden;background:var(--paper)}
  body{position:relative;font-family:"Raleway",Arial,sans-serif;color:var(--ink)}
  .page{position:absolute;width:273px;height:385px;overflow:hidden;
    background:
      radial-gradient(ellipse at 70% 18%, rgba(200,40,150,.55), transparent 60%),
      radial-gradient(ellipse at 20% 90%, rgba(150,30,120,.35), transparent 60%),
      linear-gradient(160deg,var(--plum-deep) 0%,var(--plum) 45%,var(--magenta) 100%);}
  .band{position:absolute;left:0;right:0;background:var(--band)}
  .page-title{position:absolute;left:18px;top:32px;font-family:"Poiret One",sans-serif;
    font-size:46px;line-height:1;letter-spacing:-1px;transform:scaleY(1.15);transform-origin:top left}
  .subhead{font-family:"Poiret One",sans-serif;font-size:14px;line-height:1;color:var(--ink)}
  .body-copy{font-size:5.4px;line-height:1.32;color:var(--ink-soft)}
  .photo{position:absolute;border:1.5px solid var(--ink);
    background:linear-gradient(140deg,var(--photo-a),var(--photo-b) 70%,var(--photo-a))}
  .photo.dark{background:radial-gradient(circle at 40% 50%,#b3204a,var(--photo-dark) 70%)}
  .abs{position:absolute}

  .cover-title{position:absolute;left:0;right:0;top:126px;text-align:center;font-family:"Poiret One",sans-serif;font-size:52px;line-height:1;transform:scaleY(1.2);word-spacing:10px}
  .cover-sub{position:absolute;left:0;right:0;top:290px;text-align:center;font-family:"Poiret One",sans-serif;font-size:17px;transform:scaleY(1.2)}
  .cover-copy{position:absolute;left:30px;right:30px;top:322px;text-align:center;font-size:6.3px;font-weight:600;line-height:1.32}

  .feature-list{position:absolute;left:100px;top:184px;width:160px;list-style:none}
  .feature-list li{font-size:5.6px;height:15.5px;line-height:15.5px;border-bottom:1px solid var(--rule);color:var(--ink-soft)}
  .feature-list li::before{content:"•";margin-right:4px}

  .dish{position:absolute;left:12px}
  .dish-name{font-size:10px;line-height:1.1;color:var(--ink)}
  .dish-note{font-size:4.8px;letter-spacing:.2px;color:var(--ink-soft)}
  .date-row{position:absolute;left:160px;width:105px}
  .date-row .when{font-size:6.6px}
  .date-row .inc{font-size:3.8px;color:var(--ink-soft)}
</style>
</head>
<body>

<section class="page" style="left:30px;top:66px">
  <h1 class="cover-title">EVENT TITLE</h1>
  <div class="photo dark" style="left:-2px;top:182px;width:277px;height:84px;border-left:0;border-right:0" role="img" aria-label="Close-up of wine glasses on a party table under pink lighting"></div>
  <div class="band" style="top:266px;bottom:0;background:rgba(26,4,34,.25)"></div>
  <h2 class="cover-sub">LOREM IPSUM DOLOR SIT AMET</h2>
  <p class="cover-copy">Consectetur adipiscing elit, sed do eiusmod tempor incididunt ut labore et dolore magna aliqua. Ut enim ad minim veniam, quis nostrud exercitation ullamco laboris nisi ut aliquip ex ea commodo consequat. Duis aute irure dolor in reprehenderit in voluptate velit esse</p>
</section>

<section class="page" style="left:317px;top:66px">
  <h2 class="page-title">ABOUT</h2>
  <div class="band" style="top:80px;height:134px"></div>
  <div class="abs body-copy" style="left:16px;top:92px;width:240px">
    <p>Sed ut perspiciatis unde omnis iste natus error sit voluptatem accusantium doloremque laudantium, totam rem aperiam, eaque ipsa quae ab illo inventore veritatis et quasi architecto beatae vitae dicta sunt explicabo. Nemo enim ipsam voluptatem quia voluptas sit aspernatur aut odit aut fugit, sed quia consequuntur magni dolores eos qui ratione voluptatem sequi nesciunt. Neque porro quisquam est, qui dolorem ipsum quia dolor sit amet, consectetur, adipisci velit.</p>
    <p style="margin-top:6px">Sed quia non numquam eius modi tempora incidunt ut labore et dolore magnam aliquam quaerat voluptatem. Ut enim ad minima veniam, quis nostrum exercitationem ullam corporis suscipit laboriosam, nisi ut aliquid ex ea commodi consequatur? Quis autem vel eum iure reprehenderit qui in ea voluptate velit esse quam nihil molestiae consequatur, vel illum qui dolorem eum fugiat quo voluptas nulla pariatur?</p>
  </div>
  <div class="photo dark" style="left:-2px;top:218px;width:277px;height:152px;border-left:0;border-right:0" role="img" aria-label="Cocktail glasses glowing under red and pink party lights"></div>
  <div class="abs body-copy" style="left:146px;top:237px;width:105px;height:114px;background:rgba(0,0,0,.55);padding:8px;font-size:6px;color:var(--ink)">Lorem ipsum dolor sit amet, consectetur adipiscing elit, sed do eiusmod tempor incididunt ut labore et dolore magna aliqua. Ut enim ad minim veniam, quis nostrud exercitation</div>
</section>

<section class="page" style="left:605px;top:66px">
  <h2 class="page-title">VENUE</h2>
  <div class="band" style="top:80px;bottom:0"></div>
  <div class="abs body-copy" style="left:16px;top:90px;width:112px">
    <p>Sed ut perspiciatis unde omnis iste natus error sit voluptatem accusantium doloremque laudantium, totam rem aperiam, eaque ipsa quae ab illo inventore veritatis et quasi architecto beatae vitae dicta sunt explicabo. Nemo enim ipsam voluptatem quia voluptas sit aspernatur aut odit aut fugit, sed quia consequuntur magni dolores eos qui ratione voluptatem sequi nesciunt. Neque porro quisquam est, qui dolorem ipsum quia dolor sit amet, consectetur, adipisci velit.</p>
    <p style="margin-top:6px">Sed quia non numquam eius modi tempora incidunt ut labore et dolore magnam aliquam quaerat voluptatem. Ut enim ad minima veniam, quis nostrum exercitationem ullam corporis suscipit laboriosam, nisi ut aliquid ex ea commodi consequatur?</p>
  </div>
  <h3 class="abs subhead" style="left:16px;top:270px">Dining area</h3>
  <p class="abs body-copy" style="left:16px;top:290px;width:112px">Sed ut perspiciatis unde omnis iste natus error sit voluptatem accusantium doloremque laudantium, totam rem aperiam, eaque ipsa quae ab illo inventore veritatis et quasi architecto beatae vitae dicta sunt explicabo. Nemo enim ipsam voluptatem quia voluptas sit aspernatur aut odit aut fugit, sed quia consequuntur?</p>
  <div class="photo" style="left:137px;top:91px;width:120px;height:79px" role="img" aria-label="Marquee dining room with round tables and starlit ceiling"></div>
  <div class="photo" style="left:137px;top:191px;width:120px;height:79px" role="img" aria-label="Venue interior with bar and Christmas tree"></div>
  <div class="photo" style="left:137px;top:286px;width:120px;height:79px" role="img" aria-label="Stage lit with purple spotlights"></div>
</section>

<section class="page" style="left:890px;top:66px">
  <h2 class="page-title">INCLUDED</h2>
  <div class="band" style="top:80px;bottom:0"></div>
  <div class="abs" style="left:18px;top:98px;width:80px">
    <h3 class="subhead" style="font-size:10px">Singers</h3>
    <p class="body-copy" style="margin-top:5px">Sed ut perspiciatis unde omnis iste natus error sit voluptatem accusantium doloremque laudantium, totam rem aperiam, eaque ipsa quae ab illo inventore veritatis.</p>
  </div>
  <div class="abs" style="left:100px;top:98px;width:80px">
    <h3 class="subhead" style="font-size:10px">Dancers</h3>
    <p class="body-copy" style="margin-top:5px">Sed ut perspiciatis unde omnis iste natus error sit voluptatem accusantium doloremque laudantium, totam rem aperiam, eaque ipsa quae ab illo inventore veritatis.</p>
  </div>
  <div class="abs" style="left:182px;top:98px;width:80px">
    <h3 class="subhead" style="font-size:10px">Casino</h3>
    <p class="body-copy" style="margin-top:5px">Sed ut perspiciatis unde omnis iste natus error sit voluptatem accusantium doloremque laudantium, totam rem aperiam, eaque ipsa quae ab illo inventore veritatis.</p>
  </div>
  <div class="photo" style="left:18px;top:175px;width:69px;height:45px" role="img" aria-label="Dining room with stage lighting"></div>
  <div class="photo" style="left:18px;top:224px;width:69px;height:45px" role="img" aria-label="Bar area with decorations"></div>
  <div class="photo" style="left:18px;top:273px;width:69px;height:45px" role="img" aria-label="Spotlit stage"></div>
  <div class="photo" style="left:18px;top:322px;width:69px;height:45px" role="img" aria-label="Party tables set for dinner"></div>
  <ul class="feature-list">
    <li>Exclusive Company Tables</li>
    <li>Complimentary Cloakroom</li>
    <li>Sparkling Reception</li>
    <li>Lounge Singer</li>
    <li>Photobooth</li>
    <li>Flapper Dancers</li>
    <li>Three Course Dinner</li>
    <li>Tea, Coffee &amp; Mints</li>
    <li>Fun Casino</li>
    <li style="border-bottom:0">Disco &amp; DJ</li>
  </ul>
</section>

<section class="page" style="left:30px;top:473px">
  <h2 class="page-title">GALLERY</h2>
  <div class="band" style="top:80px;bottom:0"></div>
  <div class="photo" style="left:16px;top:92px;width:114px;height:144px" role="img" aria-label="Dining tables around a decorated centrepiece"></div>
  <div class="photo" style="left:134px;top:97px;width:78px;height:89px" role="img" aria-label="Stage with spotlights"></div>
  <div class="photo" style="left:203px;top:105px;width:55px;height:95px" role="img" aria-label="Lit dining area"></div>
  <div class="photo" style="left:122px;top:185px;width:138px;height:95px" role="img" aria-label="Venue hall with Christmas tree and bar"></div>
  <div class="photo" style="left:16px;top:242px;width:113px;height:74px" role="img" aria-label="Marquee bar area"></div>
  <div class="photo" style="left:132px;top:283px;width:131px;height:76px" role="img" aria-label="Stage show with aerial performer"></div>
  <div class="photo" style="left:26px;top:315px;width:113px;height:52px;background:linear-gradient(140deg,#2a2a2a,#6a6a6a)" role="img" aria-label="Washroom with patterned wallpaper"></div>
</section>

<section class="page" style="left:317px;top:473px">
  <h2 class="page-title">MENU</h2>
  <div class="band" style="top:80px;bottom:0"></div>
  <div class="abs" style="left:148px;top:92px;width:1px;height:165px;background:var(--rule)"></div>
  <div class="dish" style="top:99px"><p class="dish-name">Haloumi Noodle Salad</p><p class="dish-note">SERVED WITH A SESAME CRACKLE</p></div>
  <div class="dish" style="top:138px"><p class="dish-name">Haloumi Noodle Salad</p><p class="dish-note">SERVED WITH A SESAME CRACKLE</p></div>
  <div class="dish" style="top:177px"><p class="dish-name">Haloumi Noodle Salad</p><p class="dish-note">SERVED WITH A SESAME CRACKLE</p></div>
  <div class="dish" style="top:216px"><p class="dish-name">Haloumi Noodle Salad</p><p class="dish-note">SERVED WITH A SESAME CRACKLE</p></div>
  <p class="abs body-copy" style="left:14px;top:257px;width:120px">Sed ut perspiciatis unde omnis iste natus error sit voluptatem accusantium doloremque laudantium, totam rem aperiam, eaque ipsa quae ab illo inventore veritatis et quasi architecto beatae vitae dicta sunt explicabo. Nemo enim ipsam voluptatem quia voluptas sit aspernatur aut odit aut fugit, sed quiaconsequatur?</p>
  <h3 class="abs subhead" style="left:160px;top:99px">Dates &amp; Price</h3>
  <div class="date-row" style="top:119px"><p class="when">Thursday 8th December - £95</p><p class="inc">INC UNLIMITED BEER, HOUSE WINE AND SOFTS</p></div>
  <div class="date-row" style="top:146px"><p class="when">Thursday 8th December - £95</p><p class="inc">INC UNLIMITED BEER, HOUSE WINE AND SOFTS</p></div>
  <div class="date-row" style="top:173px"><p class="when">Thursday 8th December - £95</p><p class="inc">INC UNLIMITED BEER, HOUSE WINE AND SOFTS</p></div>
  <div class="date-row" style="top:200px"><p class="when">Thursday 8th December - £95</p><p class="inc">INC UNLIMITED BEER, HOUSE WINE AND SOFTS</p></div>
  <div class="date-row" style="top:227px"><p class="when">Thursday 8th December - £95</p><p class="inc">INC UNLIMITED BEER, HOUSE WINE AND SOFTS</p></div>
  <h3 class="abs subhead" style="left:160px;top:260px">Drinks Package</h3>
  <p class="abs" style="left:160px;top:280px;font-size:6.4px">Fizz Upgrade - £10 +VAT</p>
</section>

<section class="page" style="left:605px;top:473px">
  <h2 class="page-title">LOCATION</h2>
  <div class="band" style="top:80px;height:142px"></div>
  <div class="abs" style="left:18px;top:95px;width:240px;height:111px;border:1.5px solid var(--ink);background:linear-gradient(135deg,var(--map-land),#d8cdbb 60%,var(--map-land))" role="img" aria-label="Street map of the venue area"></div>
  <svg class="abs" style="left:195px;top:118px" width="20" height="28" viewBox="0 0 20 28" aria-hidden="true">
    <path d="M10 0C4.5 0 0 4.4 0 9.8 0 17 10 28 10 28s10-11 10-18.2C20 4.4 15.5 0 10 0z" fill="var(--pin)"/>
    <circle cx="10" cy="9.5" r="4" fill="#3a0a22"/>
  </svg>
  <h3 class="abs subhead" style="left:21px;top:226px">Transport</h3>
  <h3 class="abs subhead" style="left:162px;top:226px">Venue Address</h3>
</section>

</body>
</html>
```